Baby and kids clothes e-commerce website

We need a clothes ecommerce page with cart and live chat available in English and Spanish. Easy to maintain. Name of the shop is TULAVEN. I need it to be really soft colour palette and easy to navigate. It needs a mobile version.

LOGO NAME "TULAVEN" and there will be a very cute teddy next to it. Picture PELUMain will be the main Bear which could have different accessories such as picture attached PELUkids.

Target Market(s)

25-40 women with kids. Clothes will be quality baby and junior clothing.

Industry/Entity Type

Baby

Logo Text

TULAVEN

Coding

Coded - Design and coding required

Number of Pages Required

5+ page

Requirements
Must have
• It must have a cart, a live chat, account section and newsletter sign up.
• Option to add discounts and change different flash details like in brelvo.com. Also blog feature and all the social Access (including Pinterest). It also needs to have the option to add a product catalogue where products can be selected.
• It will be for baby and junior clothing.
• The 5 pages will be :
• MAIN
• BABY
• GIRLS
• BOYS
• OUTLET
• It needs to have the same pages in both English and Spanish.
Nice to have
• CART
• Account section
• Newsletter sign up
• Product catalogue section
• Discounts and vouchers
• Blog Access
• Social sites including pinterest

```html
<!DOCTYPE html>
<html lang="en">
<head>
<meta charset="utf-8">
<title>TULAVEN – Baby &amp; Kids Clothes</title>
<link href="https://fonts.googleapis.com/css2?family=Montserrat:wght@400;600;700;800&family=Open+Sans:ital,wght@0,400;0,600;0,700;1,400;1,600&display=swap" rel="stylesheet">
<style>
:root{
  --blue:#4a8fe0;
  --ink:#2b2d31;
  --text:#55585e;
  --muted:#9a9da3;
  --line:#e6e7ea;
  --soft:#f6f7f9;
  --dark:#3a3d43;
  --darker:#2c2e33;
  --white:#ffffff;
}
*{box-sizing:border-box;margin:0;padding:0}
html,body{width:1200px;height:5217px;overflow:hidden}
body{font-family:"Open Sans",Arial,sans-serif;color:var(--text);background:var(--white);font-size:13px}
h1,h2,h3,h4,h5,h6{font-family:"Montserrat",Arial,sans-serif}
.wrap{width:990px;margin:0 auto;position:relative}
section,header,footer{position:relative;width:1200px;overflow:hidden}

/* header */
.site-header{height:100px;border-bottom:1px solid var(--line)}
.brand-name{position:absolute;left:105px;top:34px;font-family:"Open Sans",sans-serif;font-weight:600;font-size:26px;color:var(--ink);letter-spacing:3px;line-height:1}
.main-nav{position:absolute;left:652px;top:40px;display:flex;gap:30px}
.main-nav a{font-family:"Montserrat",sans-serif;font-size:12px;font-weight:600;color:var(--ink);text-decoration:none;letter-spacing:.5px}
.main-nav a.active{color:var(--blue)}
.btn-shop{position:absolute;left:988px;top:31px;width:104px;height:36px;border-radius:18px;background:var(--blue);color:#fff;font-family:"Montserrat",sans-serif;font-weight:700;font-size:12px;display:flex;align-items:center;justify-content:center;letter-spacing:.5px}

/* hero */
.hero{height:552px;background:linear-gradient(110deg,#c7b9a6 0%,#8c8677 30%,#6c6f63 55%,#9a9487 80%,#b8b3a8 100%)}
.hero-copy{position:absolute;left:0;right:0;top:178px;text-align:center;color:#fff}
.hero-copy h1{font-weight:800;font-size:66px;letter-spacing:1px;line-height:1}
.hero-copy p{font-family:"Montserrat",sans-serif;font-size:17px;font-weight:600;margin-top:18px;letter-spacing:1px}
.hero-actions{display:flex;justify-content:center;gap:30px;margin-top:50px}
.btn-ghost{width:92px;height:36px;border:2px solid #fff;border-radius:18px;color:#fff;font-family:"Montserrat",sans-serif;font-weight:700;font-size:12px;display:flex;align-items:center;justify-content:center;letter-spacing:.5px}
.to-top{position:absolute;right:22px;top:420px;width:28px;height:28px;background:rgba(0,0,0,.35)}

/* section titles */
.sec-title{text-align:center;position:relative}
.sec-title h2{display:inline-block;font-size:32px;font-weight:700;color:var(--ink);background:#fff;padding:0 34px;position:relative;z-index:1}
.sec-title:before{content:"";position:absolute;left:155px;right:155px;top:50%;height:1px;background:var(--line)}
.sec-sub{text-align:center;color:var(--text);font-size:13px;margin-top:14px}

/* featured */
.featured{height:772px;padding-top:86px}
.tabs{width:345px;height:38px;margin:70px auto 0;display:flex;border:1px solid var(--line)}
.tabs span{flex:1;display:flex;align-items:center;justify-content:center;font-family:"Montserrat",sans-serif;font-weight:600;font-size:12px;color:var(--ink);background:var(--soft);border-left:1px solid var(--line)}
.tabs span:first-child{border-left:0;background:#fff}
.product-row{display:flex;gap:10px;margin-top:48px}
.prod{width:240px}
.prod .thumb{height:232px}
.prod h4{font-size:14px;font-weight:700;color:var(--ink);margin-top:28px}
.prod .cat{font-size:12px;color:var(--muted);margin-top:6px}
.price{color:var(--blue);font-weight:600;font-size:14px;margin-top:6px}
.price s{color:var(--muted);font-weight:400;margin-right:6px;font-size:13px}

/* fills */
.f-baby1{background:linear-gradient(160deg,#b99b83,#e2d0c1 60%,#8a6a58)}
.f-dress-pink{background:radial-gradient(circle at 50% 55%,#e9a7a2 0 38%,#fbf2f1 39%)}
.f-shirt-white{background:radial-gradient(circle at 50% 55%,#f1f2f4 0 40%,#fff 41%),#fff;box-shadow:inset 0 0 0 1px #f3f3f3}
.f-dress-red{background:radial-gradient(circle at 50% 55%,#cf4f4f 0 40%,#fdf1f1 41%)}
.f-boy-play{background:linear-gradient(160deg,#9fb4c6,#6e8a5b 60%,#b7a27f)}
.f-girl-hat{background:linear-gradient(160deg,#c9a9c1,#8b6f91 60%,#e3d3df)}
.f-jacket{background:linear-gradient(170deg,#6f8ba3,#3a4d63 60%,#8a9aa9)}
.f-plaid{background:linear-gradient(135deg,#c43b3b,#3c5c9a 50%,#e9e1d8)}

/* collections */
.collections{height:428px;display:flex}
.coll{width:400px;height:428px;position:relative;color:#fff;text-align:center}
.coll-winter{background:linear-gradient(160deg,#b7a6b8,#b24a9a 55%,#6d4a74)}
.coll-spring{background:linear-gradient(160deg,#5fb9c4,#2e8aa6 55%,#d67a7a)}
.coll-autumn{background:linear-gradient(160deg,#d3a25b,#9a6a3e 55%,#5b4a3e)}
.coll h3{position:absolute;left:0;right:0;top:238px;font-size:34px;font-weight:700;white-space:nowrap}
.coll p{position:absolute;left:0;right:0;top:290px;font-family:"Montserrat",sans-serif;font-size:12px;font-weight:600;letter-spacing:2px}
.coll .btn-ghost{position:absolute;left:150px;top:330px;width:100px;height:34px;font-size:11px}

/* best seller */
.best{height:568px;padding-top:112px}
.best-row{display:flex;gap:4px;margin-top:40px}
.best-row div{width:194.8px;height:194px}

/* new arrivals */
.arrivals{height:1031px;padding-top:86px}
.grid{display:grid;grid-template-columns:repeat(4,240px);column-gap:10px;row-gap:18px;margin-top:30px}
.card{border:1px solid var(--line);height:364px;position:relative}
.card .thumb{height:242px}
.card h4{font-size:13px;font-weight:700;color:var(--ink);margin:16px 14px 0}
.card .meta{display:flex;justify-content:space-between;align-items:center;margin:10px 14px 0}
.card .price{margin:0;font-size:13px}
.card-foot{position:absolute;left:0;right:0;bottom:0;height:34px;border-top:1px solid var(--line);display:flex;justify-content:space-between;align-items:center;padding:0 12px;font-size:11px;color:var(--muted)}
.card-foot span{display:flex;align-items:center;gap:5px}
.ic{width:9px;height:9px;border:1.5px solid var(--muted);border-radius:2px}
.badge{position:absolute;left:12px;top:12px;width:40px;height:40px;border-radius:50%;background:var(--blue);color:#fff;font-family:"Montserrat",sans-serif;font-size:11px;font-weight:700;display:flex;align-items:center;justify-content:center}

/* testimonial */
.testimonial{height:436px;background:linear-gradient(120deg,#4c4a48,#2f2e2d 50%,#5a5550);text-align:center;color:#fff}
.avatar{width:78px;height:78px;border-radius:50%;background:#9a8a7c;border:3px solid #fff;margin:80px auto 0}
.quote{width:800px;margin:26px auto 0;font-style:italic;font-weight:600;font-size:15px;line-height:26px;letter-spacing:.5px}
.who{font-family:"Montserrat",sans-serif;font-weight:700;font-size:14px;margin-top:20px}
.dots{display:flex;justify-content:center;gap:8px;margin-top:26px}
.dots i{width:9px;height:9px;border-radius:50%;background:rgba(255,255,255,.45)}
.dots i:first-child{background:#fff}

/* widgets */
.widgets{height:363px;padding-top:26px}
.w-cols{display:grid;grid-template-columns:repeat(4,1fr);column-gap:30px}
.w-cols h5{font-size:12px;font-weight:700;color:var(--ink);letter-spacing:1px;padding-bottom:10px;border-bottom:1px solid var(--line);position:relative}
.w-cols h5:after{content:"";position:absolute;left:0;bottom:-1px;width:40px;height:2px;background:var(--blue)}
.w-item{display:flex;justify-content:space-between;margin-top:16px}
.w-item .txt{font-size:12px;color:var(--ink);line-height:18px}
.w-item .txt b{font-weight:600}
.w-item .txt small{display:block;color:var(--muted);font-size:11px}
.w-item .txt small.st{color:var(--blue)}
.w-item .sm{width:50px;height:50px;flex:none}

/* brands */
.brands{height:289px;background:var(--soft);text-align:center}
.brands h5{font-size:13px;font-weight:700;letter-spacing:3px;color:var(--ink);padding-top:74px}
.brand-row{display:flex;justify-content:center;gap:70px;margin-top:62px}
.brand-row span{font-family:"Montserrat",sans-serif;font-weight:700;font-size:24px;color:#a7a9ad;letter-spacing:3px;white-space:nowrap}

/* subscribe */
.subscribe{height:194px;background:var(--dark)}
.mail-ic{position:absolute;left:108px;top:70px;width:54px;height:54px;border-radius:50%;border:2px solid #6c7078;display:flex;align-items:center;justify-content:center}
.subscribe h3{position:absolute;left:190px;top:82px;color:#fff;font-size:22px;font-weight:700}
.sub-input{position:absolute;left:727px;top:78px;width:243px;height:38px;background:#fff;border-radius:3px;padding:0 14px;display:flex;align-items:center;font-size:12px;color:var(--muted)}
.sub-btn{position:absolute;left:980px;top:78px;width:76px;height:38px;border-radius:19px;background:var(--blue);color:#fff;font-family:"Montserrat",sans-serif;font-weight:700;font-size:12px;display:flex;align-items:center;justify-content:center}

/* footer */
.site-footer{height:410px;background:var(--darker);color:#c9cbd0}
.f-cols{position:absolute;top:56px;left:0;width:1200px}
.f-col{position:absolute;top:0}
.f-col h6{font-size:12px;font-weight:700;color:#fff;letter-spacing:1px;margin-bottom:18px}
.addr{font-size:12px;line-height:21px}
.socials{display:flex;gap:10px;margin-top:14px}
.socials i{width:14px;height:14px;border-radius:50%;background:#8d9097}
.f-prod{display:flex;gap:12px;margin-bottom:16px;font-size:12px;line-height:17px;width:210px;justify-content:space-between}
.f-prod .sm{width:48px;height:48px;flex:none}
.f-prod b{color:#fff;font-weight:600}
.f-prod .p{color:#fff}
.f-prod .p s{color:#8d9097;margin-right:5px}
.f-prod .st{color:var(--blue)}
.posts li{list-style:none;font-size:12px;margin-bottom:17px;padding-left:14px;position:relative}
.posts li:before{content:"›";position:absolute;left:0;color:var(--blue);font-weight:700}
.tags{display:flex;flex-wrap:wrap;gap:8px 14px;width:240px;font-size:11px}
.copy-bar{height:74px;background:#24262a;color:#c9cbd0;font-size:12px;display:flex;align-items:center;justify-content:center}
</style>
</head>
<body>

<svg width="0" height="0" style="position:absolute"><defs><path id="star" d="M5.5 0l1.6 3.6 3.9.4-2.9 2.6.9 3.9-3.5-2-3.5 2 .9-3.9L0 4l3.9-.4z"/></defs></svg>

<header class="site-header">
  <div class="brand-name">TULAVEN</div>
  <nav class="main-nav">
    <a href="#">HOME</a><a href="#">BABY</a><a href="#" class="active">BOYS</a><a href="#">GIRLS</a><a href="#">OUTLET</a>
  </nav>
  <div class="btn-shop">SHOP NOW</div>
</header>

<section class="hero" role="img" aria-label="Photo of a boy and a girl standing together outdoors in autumn clothes">
  <div class="hero-copy">
    <h1>NEW ARRIVALS</h1>
    <p>FOR YOUR BOY AND GIRL</p>
    <div class="hero-actions"><span class="btn-ghost">BOYS</span><span class="btn-ghost">GIRLS</span></div>
  </div>
  <div class="to-top"><svg width="28" height="28" viewBox="0 0 28 28"><path d="M9 16l5-5 5 5" stroke="#fff" stroke-width="2" fill="none"/></svg></div>
</section>

<section class="featured">
  <div class="wrap">
    <div class="sec-title"><h2>Featured Products</h2></div>
    <p class="sec-sub">Must have products from our top sellers</p>
    <div class="tabs"><span>Baby</span><span>Girl</span><span>Boy</span></div>
    <div class="product-row">
      <div class="prod"><div class="thumb f-baby1" role="img" aria-label="Baby sitting in a knitted outfit"></div><h4>Baby dress3</h4><p class="cat">Baby</p><p class="price">£102.00</p></div>
      <div class="prod"><div class="thumb f-dress-pink" role="img" aria-label="Pink baby dress"></div><h4>Baby Dress3</h4><p class="cat">Baby</p><p class="price">£34.00</p></div>
      <div class="prod"><div class="thumb f-shirt-white" role="img" aria-label="White baby shirt"></div><h4>Baby Dress1</h4><p class="cat">Baby</p><p class="price"><s>£259.00</s>£200.00</p></div>
      <div class="prod"><div class="thumb f-dress-red" role="img" aria-label="Red baby dress"></div><h4>Baby dress2</h4><p class="cat">Baby</p><p class="price">£178.00</p></div>
    </div>
  </div>
</section>

<section class="collections">
  <div class="coll coll-winter" role="img" aria-label="Child in a pink fur hat, winter collection">
    <h3>Winter Collection</h3><p>STYLISH AND WARM</p><span class="btn-ghost">SHOP NOW</span>
  </div>
  <div class="coll coll-spring" role="img" aria-label="Girl running by the water, spring collection">
    <h3>Spring Collection</h3><p>BRIGHT AND COLORFUL</p><span class="btn-ghost">SHOP NOW</span>
  </div>
  <div class="coll coll-autumn" role="img" aria-label="Boy in a jacket among autumn leaves, autumn collection">
    <h3>Autumn Collection</h3><p>COZY AND COMFORTABLE</p><span class="btn-ghost">VIEW MORE</span>
  </div>
</section>

<section class="best">
  <div class="wrap">
    <div class="sec-title"><h2>Best Seller</h2></div>
    <p class="sec-sub">Must have products from our top sellers</p>
    <div class="best-row">
      <div class="f-baby1" role="img" aria-label="Baby sitting in a knitted outfit"></div>
      <div class="f-dress-pink" role="img" aria-label="Pink baby dress"></div>
      <div class="f-shirt-white" role="img" aria-label="White baby shirt"></div>
      <div class="f-boy-play" role="img" aria-label="Boy in a cap playing outdoors"></div>
      <div class="f-girl-hat" role="img" aria-label="Girl in a pink hat"></div>
    </div>
  </div>
</section>

<section class="arrivals">
  <div class="wrap">
    <div class="sec-title"><h2>New Arrivals</h2></div>
    <div class="grid">
      <div class="card"><div class="thumb f-baby1" role="img" aria-label="Baby sitting in a knitted outfit"></div><h4>Baby dress3</h4><div class="meta"><span class="price">£102.00</span></div><div class="card-foot"><span><i class="ic"></i>Add to cart</span><span><i class="ic"></i>Details</span></div></div>
      <div class="card"><div class="thumb f-dress-pink" role="img" aria-label="Pink baby dress"></div><h4>Baby Dress3</h4><div class="meta"><span class="price">£34.00</span></div><div class="card-foot"><span><i class="ic"></i>Add to cart</span><span><i class="ic"></i>Details</span></div></div>
      <div class="card"><div class="thumb f-shirt-white" role="img" aria-label="White baby shirt"></div><span class="badge">Sale</span><h4>Baby Dress1</h4><div class="meta"><span class="price"><s>£259.00</s>£200.00</span><svg width="60" height="11" viewBox="0 0 60 11" fill="#4a8fe0"><use href="#star"/><use href="#star" x="12"/><use href="#star" x="24"/><use href="#star" x="36"/><use href="#star" x="48"/></svg></div><div class="card-foot"><span><i class="ic"></i>Add to cart</span><span><i class="ic"></i>Details</span></div></div>
      <div class="card"><div class="thumb f-boy-play" role="img" aria-label="Boy in a cap playing outdoors"></div><h4>Spring Printed Dress</h4><div class="meta"><span class="price">£37.00</span><svg width="60" height="11" viewBox="0 0 60 11" fill="#4a8fe0"><use href="#star"/><use href="#star" x="12"/><use href="#star" x="24"/><use href="#star" x="36"/><use href="#star" x="48"/></svg></div><div class="card-foot"><span><i class="ic"></i>Add to cart</span><span><i class="ic"></i>Details</span></div></div>
      <div class="card"><div class="thumb f-girl-hat" role="img" aria-label="Girl in a pink hat"></div><h4>Modern Love Tee</h4><div class="meta"><span class="price">£68.00</span></div><div class="card-foot"><span><i class="ic"></i>Add to cart</span><span><i class="ic"></i>Details</span></div></div>
      <div class="card"><div class="thumb f-dress-red" role="img" aria-label="Red baby dress"></div><h4>Baby dress2</h4><div class="meta"><span class="price">£178.00</span></div><div class="card-foot"><span><i class="ic"></i>Add to cart</span><span><i class="ic"></i>Details</span></div></div>
      <div class="card"><div class="thumb f-jacket" role="img" aria-label="Child in a blue jacket by the sea"></div><h4>Blue Clamor Jacket</h4><div class="meta"><span class="price">£153.00</span></div><div class="card-foot"><span><i class="ic"></i>Add to cart</span><span><i class="ic"></i>Details</span></div></div>
      <div class="card"><div class="thumb f-plaid" role="img" aria-label="Red and blue plaid shirt"></div><h4>Red Pale Shirt</h4><div class="meta"><span class="price">£35.00</span></div><div class="card-foot"><span><i class="ic"></i>Add to cart</span><span><i class="ic"></i>Details</span></div></div>
    </div>
  </div>
</section>

<section class="testimonial" role="img" aria-label="Dark photo of a child's bare feet on a blanket">
  <div class="avatar" role="img" aria-label="Customer portrait"></div>
  <p class="quote">Curabitur non tristique tortor. Vestibulum aliquet suscipit ipsum in volutpat. Donec vel lacinia sem, vitae semper nulla. In hac habitasse platea dictumst. Mauris consectetur est et nibh sedip hendrerit bibendum.</p>
  <p class="who">Marta Lisel, Studio Arven</p>
  <div class="dots"><i></i><i></i><i></i></div>
</section>

<section class="widgets">
  <div class="wrap w-cols">
    <div>
      <h5>FEATURED</h5>
      <div class="w-item"><p class="txt"><b>Baby Dress1</b> <s>£259.00</s><br>£200.00</p><div class="sm f-shirt-white" role="img" aria-label="White baby shirt"></div></div>
      <div class="w-item"><p class="txt"><b>Baby dress2</b> £178.00</p><div class="sm f-dress-red" role="img" aria-label="Red baby dress"></div></div>
    </div>
    <div>
      <h5>ON SALE</h5>
      <div class="w-item"><p class="txt"><b>Baby Dress1</b> <s>£259.00</s><br>£200.00</p><div class="sm f-shirt-white" role="img" aria-label="White baby shirt"></div></div>
    </div>
    <div>
      <h5>TOP RATED</h5>
      <div class="w-item"><p class="txt"><b>Spring Printed Dress</b><small class="st">★★★★★</small>£37.00</p><div class="sm f-boy-play" role="img" aria-label="Boy playing outdoors"></div></div>
      <div class="w-item"><p class="txt"><b>Baby Dress1</b><small class="st">★★★★★</small><s>£259.00</s> £200.00</p><div class="sm f-shirt-white" role="img" aria-label="White baby shirt"></div></div>
      <div class="w-item"><p class="txt"><b>Modern Love Tee</b> £68.00</p><div class="sm f-girl-hat" role="img" aria-label="Girl in a pink hat"></div></div>
    </div>
    <div>
      <h5>LATEST REVIEWS</h5>
      <div class="w-item"><p class="txt"><b>Baby Dress1</b><small class="st">★★★★★</small><small>by admin</small></p><div class="sm f-shirt-white" role="img" aria-label="White baby shirt"></div></div>
      <div class="w-item"><p class="txt"><b>Spring Printed Dress</b><small class="st">★★★★★</small><small>by admin</small></p><div class="sm f-boy-play" role="img" aria-label="Boy playing outdoors"></div></div>
    </div>
  </div>
</section>

<section class="brands">
  <h5>BRANDS LOGOS</h5>
  <div class="brand-row"><span>LUNA CRAFT</span><span>KIVO</span><span>R&amp;E</span><span>NATIVE</span><span>THE ORLA</span></div>
</section>

<section class="subscribe">
  <div class="mail-ic"><svg width="24" height="18" viewBox="0 0 24 18"><rect x="1" y="1" width="22" height="16" fill="none" stroke="#9ea2aa" stroke-width="2"/><path d="M1 1l11 9 11-9" fill="none" stroke="#9ea2aa" stroke-width="2"/></svg></div>
  <h3>Subscribe now and get special offers</h3>
  <div class="sub-input">Your email here</div>
  <div class="sub-btn">SEND</div>
</section>

<footer class="site-footer">
  <div class="f-cols">
    <div class="f-col" style="left:108px">
      <p class="addr">48 Alder Lane, Brookfield,<br>NB 20481<br>Phone: (000) 555-0148<br>Email: info@tulaven.shop<br>Web: tulaven.shop</p>
      <div class="socials"><i></i><i></i><i></i><i></i><i></i><i></i><i></i></div>
    </div>
    <div class="f-col" style="left:358px">
      <h6>TOP RATED PRODUCTS</h6>
      <div class="f-prod"><div><b>Spring Printed Dress</b><br><span class="st">★★★★★</span><br><span class="p">£37.00</span></div><div class="sm f-boy-play" role="img" aria-label="Boy playing outdoors"></div></div>
      <div class="f-prod"><div><b>Baby Dress1</b><br><span class="st">★★★★★</span><br><span class="p"><s>£259.00</s>£200.00</span></div><div class="sm f-shirt-white" role="img" aria-label="White baby shirt"></div></div>
      <div class="f-prod"><div><b>Modern Love Tee</b><br><span class="p">£68.00</span></div><div class="sm f-girl-hat" role="img" aria-label="Girl in a pink hat"></div></div>
    </div>
    <div class="f-col" style="left:615px">
      <h6>RECENT POSTS</h6>
      <ul class="posts">
        <li>Hello world!</li>
        <li>Aenean lobortis sapien enim viverra</li>
        <li>Duis ac massa semper maximus</li>
        <li>Nunc fermint nulla eu justo sem id</li>
        <li>Aliquam posuere magna eget nibh</li>
        <li>Cras at nulla ac sollicitudin rutrum</li>
      </ul>
    </div>
    <div class="f-col" style="left:865px">
      <h6>TAGS</h6>
      <div class="tags"><span>Black</span><span>Casual</span><span>Fabric</span><span>Fashion</span><span>multi-purpose</span><span>Outdoors</span><span>responsive</span><span>summer</span><span>Travel</span><span>white</span></div>
    </div>
  </div>
</footer>
<div class="copy-bar">© Copyright 2017 &nbsp;|&nbsp; TULAVEN &nbsp;|&nbsp; All Rights Reserved</div>

</body>
</html>
```